Government contracting small business needs a web design

Tarnvale Systems Inc is a veteran owned small business that delivers a full range of professional services as well as training in information technology, security and defense intelligence solutions.
We need a professional/corporate looking website where potential clients can view what services are offered.
This being a new company, there is not much that can added more than a narrative statement, stock photos and a place where potential customers and employees can make contact.
Open to ideas.
US Government
Small Business

```html
<!DOCTYPE html>
<html lang="en">
<head>
<meta charset="utf-8">
<title>Tarnvale Systems Inc</title>
<link href="https://fonts.googleapis.com/css2?family=Arimo:wght@400;700&family=Open+Sans:wght@400;600&display=swap" rel="stylesheet">
<style>
:root{
  --ink:#222;
  --grey:#5a5a5a;
  --muted:#7a7a7a;
  --light:#9a9a9a;
  --line:#dcdcdc;
  --blue:#2b8fd6;
  --blue-dark:#1b6fb4;
  --bullet:#1f5f99;
  --footer:#262626;
  --bg:#ffffff;
}
*{margin:0;padding:0;box-sizing:border-box}
html,body{width:1200px;height:1118px;overflow:hidden;background:var(--bg)}
body{font-family:"Arimo",Arial,sans-serif;color:var(--ink);position:relative}
.page{position:relative;width:1200px;height:1118px}
.abs{position:absolute}

/* header */
.brand{left:110px;top:44px;display:flex;align-items:center;gap:16px}
.brand-dot{width:62px;height:62px;border-radius:50%;background:#3a3a3a}
.brand-name{font-size:52px;font-weight:700;color:#555;letter-spacing:-1px}
.phone{left:810px;top:52px;display:flex;align-items:center;gap:10px;font-family:"Open Sans",sans-serif;font-size:21px;color:#444}
.nav{left:667px;top:106px;display:flex;height:35px;font-size:12px}
.nav a{display:block;padding:0 14px;line-height:35px;color:var(--ink);text-decoration:none}
.nav a.active{background:#ececec;border:1px solid #ddd;border-bottom:none;padding:0 18px}
.topline{left:0;top:140px;width:1200px;height:1px;background:var(--line)}

/* hero */
.hero{left:112px;top:142px;width:1002px;height:355px;background:#fbfbfb;box-shadow:0 14px 16px -12px rgba(0,0,0,.35)}
.hero-visual{position:absolute;left:0;top:0;width:560px;height:355px;background:radial-gradient(ellipse at 55% 60%,#8fd9ff 0%,#2a7cd0 25%,#0c2c6a 60%,#050d24 100%);clip-path:polygon(0 0,100% 0,86% 47%,100% 100%,0 100%)}
.hero-copy{position:absolute;left:590px;top:30px;width:370px}
.hero-title{font-size:32px;font-weight:700;color:#555}
.hero-sub{font-size:22px;color:#555;margin-top:2px}
.hero-text{font-size:12px;line-height:18px;color:var(--muted);margin-top:10px}
.hero-list{display:grid;grid-template-columns:150px 150px;row-gap:14px;column-gap:0;margin-top:14px;font-size:12px;color:var(--grey)}
.hero-list li{list-style:none;display:flex;align-items:center;gap:8px}
.btn{display:block;margin-top:22px;width:285px;height:33px;border-radius:5px;background:linear-gradient(#5fb4ec,var(--blue) 50%,var(--blue-dark));color:#fff;font-family:"Open Sans",sans-serif;font-weight:600;font-size:17px;text-align:center;line-height:33px;text-decoration:none}
.hero-arrows{position:absolute;left:760px;top:330px;width:88px;height:25px;background:#efefef;border:1px solid #ddd;display:flex}
.hero-arrows span{flex:1;display:flex;align-items:center;justify-content:center}
.hero-arrows span+span{border-left:1px solid #ddd}
.heroline{left:8px;top:496px;width:1106px;height:1px;background:var(--line)}

/* main */
.main{left:171px;top:538px;width:545px}
.main h1{font-size:17px;font-weight:400;color:var(--ink)}
.intro{font-size:10px;line-height:18px;color:var(--grey);margin-top:18px}
.feature{display:flex;gap:22px;margin-top:8px}
.photo{width:168px;height:168px;flex:none;border:1px solid #ddd;background:linear-gradient(135deg,#3c5a8c,#c9a58a 50%,#b33a3a)}
.feature h2,.block h2{font-size:11px;font-weight:700;color:var(--ink)}
.feature p{font-size:12px;line-height:18.5px;color:var(--muted);margin-top:22px}
.block{margin-top:18px;margin-left:-7px}
.block p{font-size:12px;line-height:18.5px;color:var(--muted);margin-top:4px}
.quote{left:163px;top:929px;width:549px;height:108px;border:1px solid #e4e4e4;background:#f4f4f4;padding:22px 26px}
.quote-mark{position:absolute;left:14px;top:-6px;font-size:90px;color:#e2e2e2;font-family:Georgia,serif}
.quote p{position:relative;font-size:11px;line-height:19px;color:var(--muted)}
.quote cite{position:relative;display:block;text-align:right;font-size:11px;font-weight:700;color:var(--grey);margin-top:12px}

/* sidebar */
.side{left:751px;top:540px;width:240px}
.side h3{font-size:17px;font-weight:400;color:var(--ink)}
.services{margin-top:8px}
.services li{list-style:none;display:flex;align-items:center;gap:14px;height:27.5px;font-size:11px;color:var(--grey)}
.more{display:inline-block;margin-top:6px;margin-left:-4px;padding:3px 7px;background:#d8d8d8;color:#fff;font-size:10px;font-weight:700;border-radius:2px}
.loc{margin-top:10px;margin-left:-4px}
.map{width:224px;height:120px;margin-top:6px;background:linear-gradient(135deg,#efe6c8,#f3d37a 55%,#e8e0c8)}
.contact{font-size:9px;line-height:15.5px;color:var(--light);margin-top:8px;letter-spacing:.3px}
.contact .dark{color:#555}

/* footer */
.footer{left:0;top:1058px;width:1200px;height:60px;background:var(--footer);padding:12px 0 0 163px;color:#fff;font-size:11px}
.footer nav a{color:#fff;text-decoration:none}
.footer nav span{margin:0 14px}
.footer small{display:block;font-size:11px;color:#aaa;margin-top:2px}
</style>
</head>
<body>
<div class="page">
  <div class="abs brand"><span class="brand-dot"></span><span class="brand-name">Tarnvale Systems</span></div>

  <div class="abs phone">
    <svg width="34" height="24" viewBox="0 0 34 24"><path d="M3 8c0-5 28-5 28 0v3h-7V8H10v3H3z" fill="#333"/><rect x="7" y="11" width="20" height="12" rx="2" fill="#333"/><circle cx="17" cy="17" r="3" fill="#777"/></svg>
    <span>1(800) 555 0142</span>
  </div>

  <nav class="abs nav">
    <a class="active" href="#">Home</a><a href="#">About Us</a><a href="#">Service</a><a href="#">Blog</a><a href="#">Contact us</a>
  </nav>
  <div class="abs topline"></div>

  <section class="abs hero">
    <div class="hero-visual" role="img" aria-label="Figures of people made of glowing blue digits"></div>
    <div class="hero-copy">
      <div class="hero-title">Tarnvale Systems Inc</div>
      <div class="hero-sub">veteran owned small business</div>
      <p class="hero-text">Curabitur dignissim, purus id posuere Vehicula, ipsum risus placerat lacus, vel interdum enim augue at au gue.<br>Sed iaculis enim in lacus. Sed consequat ornare quam. Vivamus pulvinar sollicitudin metus.</p>
      <ul class="hero-list">
        <li><svg width="11" height="11"><circle cx="5.5" cy="5.5" r="5.5" fill="#1f5f99"/><path d="M3 5.5h5M5.5 3v5" stroke="#fff" stroke-width="1.5"/></svg>Curabitur dignissim</li>
        <li><svg width="11" height="11"><circle cx="5.5" cy="5.5" r="5.5" fill="#1f5f99"/><path d="M3 5.5h5M5.5 3v5" stroke="#fff" stroke-width="1.5"/></svg>Curabitur dignissim</li>
        <li><svg width="11" height="11"><circle cx="5.5" cy="5.5" r="5.5" fill="#1f5f99"/><path d="M3 5.5h5M5.5 3v5" stroke="#fff" stroke-width="1.5"/></svg>Curabitur dignissim</li>
        <li><svg width="11" height="11"><circle cx="5.5" cy="5.5" r="5.5" fill="#1f5f99"/><path d="M3 5.5h5M5.5 3v5" stroke="#fff" stroke-width="1.5"/></svg>Curabitur dignissim</li>
      </ul>
      <a class="btn" href="#">Learn more about us</a>
    </div>
    <div class="hero-arrows">
      <span><svg width="10" height="6"><path d="M1 1l4 4 4-4" fill="none" stroke="#aaa" stroke-width="2"/></svg></span>
      <span><svg width="10" height="6"><path d="M1 5l4-4 4 4" fill="none" stroke="#1f5f99" stroke-width="2"/></svg></span>
    </div>
  </section>
  <div class="abs heroline"></div>

  <main class="abs main">
    <h1>Welcome to Government contracting small business company</h1>
    <p class="intro">Curabitur dignissim, purus id posuere Vehicula, ipsum risus placerat lacus, vel interdum enim augue at au gue.<br>Sed iaculis enim in lacus. Sed consequat ornare quam. Vivamus pulvinar sollicitudin metus.<br>Vivamus id risus sed pede convallis fringilla.</p>
    <div class="feature">
      <div class="photo" role="img" aria-label="Two hands shaking in front of a flag"></div>
      <div>
        <h2>Government contracting small business</h2>
        <p>Curabitur dignissim, purus id posuere Vehicula, ipsum risus placerat lacus, vel interdum enim augue at au gue.<br>Sed iaculis enim in lacus. Sed consequat ornare quam. Vivamus pulvinar sollicitudin metus.<br>Vivamus id risus sed pede convallis fringilla.Sed iaculis enim in lacus. Sed consequat ornare quam. Vivamus pulvinar sollicitu-din metus.</p>
      </div>
    </div>
    <div class="block">
      <h2>Government contracting small business</h2>
      <p>Curabitur dignissim, purus id posuere Vehicula, ipsum risus placerat lacus, vel interdum enim augue at au gue. Sed iaculis enim in lacus. Sed consequat ornare quam. Vivamus pulvinar sollicitudin metus. Vivamus id risus sed pede convallis fringilla.</p>
    </div>
  </main>

  <blockquote class="abs quote">
    <span class="quote-mark">&ldquo;</span>
    <p>"It is a long established fact that a reader will be distracted by the readable content of a page when looking at its layout.Content here, content here', making it look like readable English."</p>
    <cite>Dana Wellbrook - client</cite>
  </blockquote>

  <aside class="abs side">
    <h3>Services</h3>
    <ul class="services">
      <li><svg width="11" height="11"><circle cx="5.5" cy="5.5" r="5.5" fill="#1f5f99"/><path d="M3 5.5h5M5.5 3v5" stroke="#fff" stroke-width="1.5"/></svg>Service 1</li>
      <li><svg width="11" height="11"><circle cx="5.5" cy="5.5" r="5.5" fill="#1f5f99"/><path d="M3 5.5h5M5.5 3v5" stroke="#fff" stroke-width="1.5"/></svg>Service 2</li>
      <li><svg width="11" height="11"><circle cx="5.5" cy="5.5" r="5.5" fill="#1f5f99"/><path d="M3 5.5h5M5.5 3v5" stroke="#fff" stroke-width="1.5"/></svg>Service 3</li>
      <li><svg width="11" height="11"><circle cx="5.5" cy="5.5" r="5.5" fill="#1f5f99"/><path d="M3 5.5h5M5.5 3v5" stroke="#fff" stroke-width="1.5"/></svg>Service 4</li>
      <li><svg width="11" height="11"><circle cx="5.5" cy="5.5" r="5.5" fill="#1f5f99"/><path d="M3 5.5h5M5.5 3v5" stroke="#fff" stroke-width="1.5"/></svg>Service 5</li>
      <li><svg width="11" height="11"><circle cx="5.5" cy="5.5" r="5.5" fill="#1f5f99"/><path d="M3 5.5h5M5.5 3v5" stroke="#fff" stroke-width="1.5"/></svg>Service 6</li>
    </ul>
    <span class="more">more service</span>
    <h3 class="loc">Location</h3>
    <div class="map" role="img" aria-label="Street map showing the office location"></div>
    <p class="contact">Address:<br>48 Harlow Street, P.O. Box 4410<br>Brenton, VA 22001-4410<br><br>Telephone:+1 555 014 2260<br>FAX:+1 555 014 2261<br><span class="dark">E-mail: contact@tarnvale.example<br>Website: www.tarnvale.example</span></p>
  </aside>

  <footer class="abs footer">
    <nav><a href="#">Home</a><span>|</span><a href="#">About Us</a><span>|</span><a href="#">Service</a><span>|</span><a href="#">Blog</a><span>|</span><a href="#">Contact us</a></nav>
    <small>Government contracting &nbsp;@ 2012 All Rights Reserved.</small>
  </footer>
</div>
</body>
</html>
```